Professional IT Company Letterhead

We need a new letterhead design to incorporate our new login and business card design recently received here on Sketch Guild. We want the same look and feel as the other two accepted projects. We want a professional and clean design.

Target Market(s)

Medical/Dental and Professional Services Businesses (CPA, Attorney, Architect etc)

Industry/Entity Type

Business

Requirements
Must have
• Clean and professional, consistent brand with our current design of our new logo and business cards.
Nice to have
• Would like to also be able to use the design on our newsletter header

```html
<!DOCTYPE html>
<html lang="en">
<head>
<meta charset="utf-8">
<title>Tidewell Letterhead</title>
<link rel="stylesheet" href="https://fonts.googleapis.com/css2?family=Open+Sans:wght@400;600;700&family=Quicksand:wght@500&display=swap">
<style>
  :root {
    --brand-blue: #1f9ad6;
    --name-blue: #1b75bb;
    --divider-blue: #3b8fd0;
    --ink: #333333;
    --title-grey: #444444;
    --paper: #ffffff;
    --water-light: #d6ecf8;
    --water-mid: #7cc0e8;
    --water-deep: #2a86c8;
  }
  * { margin: 0; padding: 0; box-sizing: border-box; }
  html, body { width: 839px; height: 1200px; overflow: hidden; background: var(--paper); }
  .letterhead {
    position: relative;
    width: 839px;
    height: 1200px;
    background: var(--paper);
    font-family: "Open Sans", Arial, sans-serif;
    color: var(--ink);
  }
  .brand {
    position: absolute;
    left: 108px;
    top: 88px;
  }
  .brand-row {
    display: flex;
    align-items: center;
    gap: 26px;
  }
  .brand-mark {
    width: 74px;
    height: 74px;
    border-radius: 50%;
    background: var(--brand-blue);
  }
  .brand-name {
    font-family: "Open Sans", Arial, sans-serif;
    font-weight: 600;
    font-size: 58px;
    line-height: 1;
    letter-spacing: -1px;
    color: var(--brand-blue);
  }
  .brand-tagline {
    margin-top: 14px;
    font-family: "Quicksand", Arial, sans-serif;
    font-weight: 500;
    font-size: 14.5px;
    letter-spacing: 1.1px;
    color: var(--brand-blue);
  }
  .sender {
    position: absolute;
    left: 591px;
    top: 123px;
    height: 62px;
    padding-left: 21px;
    border-left: 1.5px solid var(--divider-blue);
  }
  .sender-name {
    font-size: 25px;
    font-weight: 400;
    color: var(--name-blue);
    line-height: 1.1;
    margin-top: 6px;
  }
  .sender-title {
    font-size: 13.5px;
    font-weight: 600;
    color: var(--title-grey);
    margin-top: 4px;
    letter-spacing: -0.2px;
  }
  .water-band {
    position: absolute;
    left: 0;
    top: 1024px;
    width: 839px;
    height: 72px;
  }
  .contact {
    position: absolute;
    left: 0;
    top: 1106px;
    width: 839px;
    text-align: center;
    font-size: 11.6px;
    font-weight: 600;
    color: var(--ink);
    letter-spacing: -0.2px;
    line-height: 17px;
  }
  .contact .sep {
    display: inline-block;
    width: 2.5px;
    height: 13px;
    background: var(--divider-blue);
    vertical-align: -2px;
    margin: 0 3px;
  }
</style>
</head>
<body>
<div class="letterhead">
  <header class="brand">
    <div class="brand-row">
      <div class="brand-mark"></div>
      <div class="brand-name">tidewell</div>
    </div>
    <div class="brand-tagline">IT Support for Medical &amp; Dental Practices</div>
  </header>

  <div class="sender">
    <div class="sender-name">Dana Mercer</div>
    <div class="sender-title">President and CEO</div>
  </div>

  <svg class="water-band" viewBox="0 0 839 72" role="img" aria-label="Splash of clear blue water running across the page" preserveAspectRatio="none">
    <defs>
      <linearGradient id="waterFill" x1="0" y1="0" x2="0" y2="1">
        <stop offset="0" stop-color="var(--water-light)"/>
        <stop offset="0.55" stop-color="var(--water-mid)"/>
        <stop offset="1" stop-color="var(--water-deep)"/>
      </linearGradient>
    </defs>
    <path d="M0 26 C80 18 160 34 250 24 C320 16 380 30 460 22 C560 14 640 30 720 22 C770 18 810 20 839 18 L839 44 C760 48 680 40 600 46 C500 52 420 42 330 48 C230 54 130 44 0 50 Z" fill="url(#waterFill)"/>
  </svg>

  <footer class="contact">
    <div>1820 Harbor Pines Lane, Ste. B, Lakemont, Texas 77001<span class="sep"></span>ph: 281 555 0142<span class="sep"></span>f: 281 555 0178<span class="sep"></span>danamercer@tidewelltech.com</div>
    <div>www.tidewelltech.com</div>
  </footer>
</div>
</body>
</html>
```